Corvale Homes

To produce a business card design for our newly established house building and development company, We have had a logo design done please see attached, our slogan is "Crafting the place you call home"
Contact Information for Business Card
Adress on card needs to Read - 58 Elmsworth Lane, Harlowmere, Westvale WV7 4QT. Director name Dean Vascotti
Requirements
Must have
- Web adress is www.corvale-homes.co.uk
- Email address is info@corvale-homes.co.uk
- phone number 07700 900417

```html
<!DOCTYPE html>
<html lang="en">
<head>
<meta charset="utf-8">
<title>Corvale Homes – Business Card</title>
<link rel="stylesheet" href="https://fonts.googleapis.com/css2?family=Montserrat:wght@800&family=Open+Sans:wght@400;600&display=swap">
<style>
  :root {
    --green: #7cc242;
    --grey-panel: #8e8e8e;
    --grey-rule: #9a9a9a;
    --ink: #3a3a3a;
    --paper: #fbfbfa;
    --backdrop: #e9ecec;
    --white: #ffffff;
  }
  * { box-sizing: border-box; margin: 0; padding: 0; }
  html, body {
    width: 1116px; height: 1200px; overflow: hidden;
    background: var(--backdrop);
  }
  .sheet {
    width: 1116px; height: 1200px;
    display: flex; flex-direction: column; align-items: center; justify-content: center;
    gap: 56px;
  }
  .card {
    position: relative;
    width: 900px; height: 514px;
    background: var(--paper);
    box-shadow: 0 6px 18px rgba(0,0,0,0.12);
    overflow: hidden;
  }

  /* Front */
  .card--front {
    display: flex; flex-direction: column; align-items: center; justify-content: center;
  }
  .brand-name {
    font-family: "Montserrat", sans-serif;
    font-weight: 800;
    color: var(--green);
    text-transform: uppercase;
    letter-spacing: 2px;
    line-height: 1;
    text-align: center;
    white-space: nowrap;
  }
  .card--front .brand-name { font-size: 66px; }
  .brand-rule { height: 2px; background: var(--grey-rule); }
  .card--front .brand-rule { width: 500px; margin-top: 22px; }
  .slogan {
    margin-top: 12px;
    font-family: "Open Sans", sans-serif;
    font-weight: 600;
    font-size: 13px;
    letter-spacing: 7px;
    color: var(--green);
    text-transform: uppercase;
    white-space: nowrap;
  }

  /* Back */
  .back-panel { position: absolute; inset: 0; }
  .contact-list {
    position: absolute; left: 80px; top: 150px;
    list-style: none;
    display: flex; flex-direction: column; gap: 52px;
  }
  .contact-item {
    display: flex; align-items: center; gap: 22px;
    font-family: "Open Sans", sans-serif;
    font-size: 17px; line-height: 1.45;
    color: var(--white);
  }
  .contact-icon { flex: 0 0 44px; width: 44px; height: 44px; }
  .identity {
    position: absolute; left: 545px; top: 130px; width: 330px;
    display: flex; flex-direction: column; align-items: center;
  }
  .identity .brand-name { font-size: 28px; letter-spacing: 1px; }
  .identity .brand-rule { width: 290px; margin-top: 14px; }
  .person-name {
    margin-top: 40px;
    font-family: "Open Sans", sans-serif; font-size: 17px;
    color: var(--ink); text-transform: uppercase; letter-spacing: 0.5px;
  }
  .person-role {
    margin-top: 2px;
    font-family: "Open Sans", sans-serif; font-size: 13px;
    color: var(--ink);
  }
</style>
</head>
<body>
<main class="sheet">

  <section class="card card--front" aria-label="Business card front">
    <h1 class="brand-name">Corvale Homes</h1>
    <div class="brand-rule"></div>
    <p class="slogan">Crafting the place you call home</p>
  </section>

  <section class="card card--back" aria-label="Business card back">
    <svg class="back-panel" width="900" height="514" viewBox="0 0 900 514" aria-hidden="true">
      <path d="M30 30 H430 C470 170 470 330 505 484 H30 Z" fill="var(--grey-panel)"/>
    </svg>

    <ul class="contact-list">
      <li class="contact-item">
        <svg class="contact-icon" viewBox="0 0 44 44" aria-hidden="true">
          <circle cx="22" cy="22" r="21" fill="var(--green)"/>
          <path d="M22 11a8 8 0 0 0-8 8c0 6 8 14 8 14s8-8 8-14a8 8 0 0 0-8-8z" fill="var(--white)"/>
          <circle cx="22" cy="19" r="3" fill="var(--green)"/>
        </svg>
        <span>58 Elmsworth Lane, Harlowmere,<br>Westvale WV7 4QT</span>
      </li>
      <li class="contact-item">
        <svg class="contact-icon" viewBox="0 0 44 44" aria-hidden="true">
          <circle cx="22" cy="22" r="21" fill="var(--green)"/>
          <g fill="none" stroke="var(--white)" stroke-width="2">
            <circle cx="22" cy="22" r="11"/>
            <ellipse cx="22" cy="22" rx="5" ry="11"/>
            <path d="M11 22h22M13 16h18M13 28h18"/>
          </g>
        </svg>
        <span>www.corvale-homes.co.uk<br>info@corvale-homes.co.uk</span>
      </li>
      <li class="contact-item">
        <svg class="contact-icon" viewBox="0 0 44 44" aria-hidden="true">
          <circle cx="22" cy="22" r="21" fill="var(--green)"/>
          <path d="M15 12l5 0 2 6-3 2c1.5 3 3.5 5 6 6l2-3 6 2v5c0 1-1 2-2 2-10 0-18-8-18-18 0-1 1-2 2-2z" fill="var(--white)"/>
        </svg>
        <span>07700 900417</span>
      </li>
    </ul>

    <div class="identity">
      <h2 class="brand-name">Corvale Homes</h2>
      <div class="brand-rule"></div>
      <p class="person-name">Dean Vascotti</p>
      <p class="person-role">Director</p>
    </div>
  </section>

</main>
</body>
</html>
```